Dental Health Door hanger for contest to attract new patients

We are a group dental practice located in Burlington, Ontario, Canada. We are looking to bring in new patients and are targeting a new subdivision as well as established neighbourhoods around it.

The door hanger we require is for a contest are offering that will run for approx. 6 months to win a $1000.00 travel gift card. The individual must come in person to drop off the ballot and during that time they will get a tour of the practice and meet key people. There is no requirement for them to make an appointment but that is the ultimate goal.

I have included:
- a picture we typically use, however it is not required (female smiling)
- Our logo with "your city your dentists" below it. We want that tagline removed
- our other logo
- the excel version of the map created to our location
- the current one attempted on our own and is missing something - like the concept but not the total look/ feel

The final design should make the person want to come in and book an appointment with us and at the very least call to schedule something with a dentist.

Target Market(s)

New subdivision and surrounding area for new patients

Industry/Entity Type

Dental Clinic

Colors

Designer to choose colors to be used in the design.

Requirements
Must have
• Our address is 1846 Pemberly Road, Burlington, Ontario L7M 2K8. Our phone number is 905-482-7150. We are located on the 3rd floor of the Corvane Family Health Centre.
Nice to have
• We only need to have a logo, our address, a ballot of some sort on the door hanger and the details about the contest, the rest is up to you. We are moving towards the slogan "what makes you smile" at some point so this can be incorporated if it works with the overall design.
Should not have
• Fluorescent colours

```html
<!DOCTYPE html>
<html lang="en">
<head>
<meta charset="utf-8">
<title>Brightwell Dental Group – Contest Door Hanger</title>
<link href="https://fonts.googleapis.com/css2?family=Oswald:wght@400;500;600&family=Open+Sans:wght@400;600;700&display=swap" rel="stylesheet">
<style>
  :root {
    --brand-blue: #3a8de6;
    --brand-blue-dark: #2b73c4;
    --ink: #1b1b1b;
    --panel-black: #141414;
    --paper: #ffffff;
    --text-grey: #4a4a4a;
    --line-grey: #b9b9b9;
    --stage: #f1f1f1;
    --label-grey: #c8c8c8;
  }
  * { box-sizing: border-box; margin: 0; padding: 0; }
  html, body { width: 1200px; height: 1080px; overflow: hidden; }
  body {
    background: var(--stage);
    font-family: "Open Sans", sans-serif;
    position: relative;
  }
  .hanger {
    position: absolute;
    top: 50px;
    width: 300px;
    height: 840px;
  }
  .hanger--front { left: 220px; }
  .hanger--back { left: 680px; }
  .hanger__shape {
    position: absolute; inset: 0;
    width: 300px; height: 840px;
  }
  .hanger__body {
    position: absolute;
    left: 0; right: 0; top: 250px; bottom: 0;
    display: flex; flex-direction: column;
  }

  /* FRONT */
  .brand {
    display: flex; align-items: center; gap: 12px;
    padding: 10px 24px 18px;
    color: var(--paper);
  }
  .brand__mark {
    width: 26px; height: 26px;
    border: 2px solid var(--paper);
    flex: none;
  }
  .brand__name {
    font-family: "Open Sans", sans-serif;
    font-weight: 400;
    font-size: 21px;
    line-height: 1.1;
    letter-spacing: 0.5px;
  }
  .photo {
    margin: 0 0 0 18px;
    height: 190px;
    background: linear-gradient(135deg, #3a3532 0%, #8c7a6c 45%, #d8d2cc 100%);
  }
  .prize {
    margin: 18px 18px 22px;
    flex: 1;
    background: var(--panel-black);
    color: var(--paper);
    display: flex; flex-direction: column; align-items: center; justify-content: center;
    font-family: "Oswald", sans-serif;
    text-align: center;
  }
  .prize__lead {
    color: var(--brand-blue);
    font-size: 30px; font-weight: 500; letter-spacing: 0.5px;
    text-transform: uppercase;
  }
  .prize__amount {
    font-size: 96px; font-weight: 600; line-height: 1;
    color: #e6e6e6;
    margin: 6px 0 8px;
  }
  .prize__item {
    color: var(--brand-blue);
    font-size: 32px; font-weight: 500;
  }

  /* BACK */
  .invite {
    text-align: center;
    color: var(--paper);
    font-family: "Oswald", sans-serif;
    padding: 0 14px 12px;
  }
  .invite__line { font-size: 22px; font-weight: 400; line-height: 1.15; }
  .invite__call { font-size: 25px; font-weight: 500; text-transform: uppercase; line-height: 1.15; }
  .map {
    margin: 0 16px;
    height: 170px;
    background: linear-gradient(180deg, #ffffff 0%, #eeeeee 100%);
  }
  .visit {
    margin: 12px 16px 0;
    background: var(--paper);
    padding: 14px 12px 12px;
    text-align: center;
    font-size: 12px;
    line-height: 1.45;
    color: var(--text-grey);
  }
  .visit__place { color: var(--brand-blue); font-weight: 700; }
  .visit__row { display: flex; align-items: center; justify-content: center; gap: 5px; margin-top: 3px; }
  .visit__phone {
    display: inline-flex; align-items: center; gap: 5px;
    background: var(--brand-blue); color: var(--paper);
    border-radius: 10px; padding: 0 9px; font-weight: 600;
  }
  .icon { width: 11px; height: 11px; flex: none; }
  .ballot {
    flex: 1;
    margin-top: 12px;
    background: var(--paper);
    padding: 18px 18px 16px;
    display: flex; flex-direction: column; justify-content: space-evenly;
    font-size: 11px; color: var(--text-grey);
  }
  .ballot__row { display: flex; align-items: flex-end; gap: 6px; }
  .ballot__label { white-space: nowrap; }
  .ballot__line { flex: 1; border-bottom: 1px solid var(--line-grey); height: 12px; }

  .side-label {
    position: absolute;
    top: 950px;
    width: 300px;
    text-align: center;
    font-family: "Oswald", sans-serif;
    font-weight: 500;
    font-size: 60px;
    color: var(--label-grey);
    letter-spacing: 1px;
  }
  .side-label--front { left: 220px; }
  .side-label--back { left: 680px; }
</style>
</head>
<body>

<section class="hanger hanger--front">
  <svg class="hanger__shape" viewBox="0 0 300 840" aria-hidden="true">
    <path fill-rule="evenodd" fill="var(--brand-blue)"
      d="M0 150 A150 150 0 0 1 300 150 L300 840 L0 840 Z
         M150 70 A68 68 0 1 0 150.01 70 Z"/>
  </svg>
  <div class="hanger__body">
    <div class="brand">
      <span class="brand__mark"></span>
      <span class="brand__name">Brightwell<br>Dental Group</span>
    </div>
    <div class="photo" role="img" aria-label="Photo of a smiling woman in a winter hat"></div>
    <div class="prize">
      <div class="prize__lead">Enter to win a</div>
      <div class="prize__amount">$1000</div>
      <div class="prize__item">Travel Gift Card</div>
    </div>
  </div>
</section>

<section class="hanger hanger--back">
  <svg class="hanger__shape" viewBox="0 0 300 840" aria-hidden="true">
    <path fill-rule="evenodd" fill="var(--brand-blue)"
      d="M0 150 A150 150 0 0 1 300 150 L300 840 L0 840 Z
         M150 70 A68 68 0 1 0 150.01 70 Z"/>
  </svg>
  <div class="hanger__body">
    <div class="invite">
      <div class="invite__line">Stop By Meet The Team</div>
      <div class="invite__call">Enter to win!</div>
    </div>
    <div class="map" role="img" aria-label="Street map showing the clinic location near nearby main roads"></div>
    <div class="visit">
      Come in person to submit<br>
      your ballot at our Pemberly Road location,<br>
      conveniently located on<br>
      the 3rd floor of the<br>
      <span class="visit__place">Corvane Family Health Centre</span>
      <div class="visit__row">
        <svg class="icon" viewBox="0 0 12 12" aria-hidden="true"><path fill="var(--brand-blue)" d="M6 0a4 4 0 0 0-4 4c0 3 4 8 4 8s4-5 4-8a4 4 0 0 0-4-4zm0 5.6A1.6 1.6 0 1 1 6 2.4a1.6 1.6 0 0 1 0 3.2z"/></svg>
        <span>1846 Pemberly Road, Burlington, Ontario L7M 2K8</span>
      </div>
      <div class="visit__row">
        <span class="visit__phone">
          <svg class="icon" viewBox="0 0 12 12" aria-hidden="true"><path fill="#fff" d="M2.4 0.8l1.8 0 .8 2.4-1.2 1a7 7 0 0 0 3.9 3.9l1-1.2 2.4.8v1.8c0 .7-.6 1.2-1.3 1.1A10 10 0 0 1 1.3 2.1C1.2 1.4 1.7.8 2.4.8z"/></svg>
          905-482-7150
        </span>
      </div>
      <div class="visit__row">www.brightwelldental.ca</div>
    </div>
    <div class="ballot">
      <div class="ballot__row"><span class="ballot__label">Name</span><span class="ballot__line"></span></div>
      <div class="ballot__row"><span class="ballot__label">Address</span><span class="ballot__line"></span></div>
      <div class="ballot__row"><span class="ballot__label">City</span><span class="ballot__line"></span><span class="ballot__label">Postal Code</span><span class="ballot__line"></span></div>
      <div class="ballot__row"><span class="ballot__label">Phone</span><span class="ballot__line"></span></div>
      <div class="ballot__row"><span class="ballot__label">Email Address</span><span class="ballot__line"></span></div>
    </div>
  </div>
</section>

<div class="side-label side-label--front">FRONT</div>
<div class="side-label side-label--back">BACK</div>

</body>
</html>
```